FR banner

we need a banner design (36"x120" horizontal) that will be displayed on a local high school baseball field. My company ( Crestwell Prints Co) has been producing signage for the Fernmoor Ridge community since 2009. We would like to communicate that we do more than banners. The final design should include the slogan "Signs Shirts Swag" and our Logo.

Target Market(s)

companies, teams, events, shirt and other marketing items.

Industry/Entity Type

Sign, Print,

Font styles to use
Sans Serif

Requirements
Should not have
• no baseball content.

```html
<!DOCTYPE html>
<html lang="en">
<head>
<meta charset="utf-8">
<title>Crestwell Prints Co — Signs Shirts Swag Banner</title>
<link href="https://fonts.googleapis.com/css2?family=Kalam:wght@700&family=Oswald:wght@700&display=swap" rel="stylesheet">
<style>
  :root {
    --page-bg: #eceef1;
    --banner-black: #000000;
    --ring-cyan: #0b9fe0;
    --ring-indigo: #2f2f9a;
    --disc-white: #ffffff;
    --ink: #1c1c1c;
    --slogan-white: #ffffff;
    --slogan-glow: #1e7fe6;
    --rule-white: #e9e9e9;
    --wave-blue: rgba(20, 120, 200, 0.22);
  }
  * { margin: 0; padding: 0; box-sizing: border-box; }
  html, body {
    width: 900px; height: 1200px; overflow: hidden;
    background: var(--page-bg);
  }
  .canvas {
    position: relative; width: 900px; height: 1200px;
  }
  .banner {
    position: absolute; left: 279px; top: 30px;
    width: 342px; height: 1140px;
    background: var(--banner-black);
    box-shadow: 0 6px 18px rgba(0,0,0,0.25);
    overflow: hidden;
  }
  .banner__waves {
    position: absolute; inset: 0;
    background:
      radial-gradient(ellipse 90px 380px at 0% 22%, var(--wave-blue), transparent 70%),
      radial-gradient(ellipse 110px 420px at 100% 58%, var(--wave-blue), transparent 70%),
      radial-gradient(ellipse 120px 260px at 0% 88%, var(--wave-blue), transparent 70%);
  }
  .ring {
    position: absolute; left: 50%; transform: translate(-50%, -50%);
    border-radius: 50%;
    background: conic-gradient(from 200deg, var(--ring-indigo), var(--ring-cyan), var(--ring-cyan), var(--ring-indigo));
    padding: 5px;
  }
  .ring__inner {
    width: 100%; height: 100%; border-radius: 50%;
    background: var(--banner-black);
    display: flex; align-items: center; justify-content: center;
  }
  .brand { width: 226px; height: 226px; top: 157px; }
  .brand .ring__inner { background: var(--disc-white); }
  .brand__name {
    font-family: "Oswald", "Arial Narrow", sans-serif;
    font-weight: 700; font-size: 30px; line-height: 1.05;
    color: var(--ink); text-align: center; text-transform: uppercase;
  }
  .service-icon { width: 136px; height: 136px; }
  .service-icon--signs { top: 388px; }
  .service-icon--shirts { top: 662px; }
  .service-icon--swag { top: 934px; }
  .service-icon__art {
    width: 74px; height: 74px; border-radius: 10px;
    background: radial-gradient(circle, #2a2a2a, #111);
  }
  .slogan-word {
    position: absolute; left: 0; width: 100%; text-align: center;
    font-family: "Kalam", "Comic Sans MS", sans-serif;
    font-weight: 700; font-size: 74px; line-height: 1;
    color: var(--slogan-white);
    text-shadow: 0 0 2px var(--slogan-glow), 2px 2px 0 var(--slogan-glow);
  }
  .slogan-word--signs { top: 470px; }
  .slogan-word--shirts { top: 742px; font-size: 78px; }
  .slogan-word--swag { top: 1012px; }
  .divider {
    position: absolute; left: 47px; width: 247px; height: 1px;
    background: var(--rule-white);
  }
  .divider--first { top: 569px; }
  .divider--second { top: 843px; }
</style>
</head>
<body>
<main class="canvas">
  <section class="banner" aria-label="Crestwell Prints Co banner: Signs, Shirts, Swag">
    <div class="banner__waves" role="img" aria-label="Flowing blue line-wave background pattern"></div>

    <div class="ring brand">
      <div class="ring__inner">
        <p class="brand__name">Crestwell<br>Prints Co</p>
      </div>
    </div>

    <div class="ring service-icon service-icon--signs">
      <div class="ring__inner">
        <div class="service-icon__art" role="img" aria-label="Line drawing of a sign board and a hanging sign"></div>
      </div>
    </div>
    <h2 class="slogan-word slogan-word--signs">Signs</h2>
    <div class="divider divider--first"></div>

    <div class="ring service-icon service-icon--shirts">
      <div class="ring__inner">
        <div class="service-icon__art" role="img" aria-label="Line drawing of two t-shirts"></div>
      </div>
    </div>
    <h2 class="slogan-word slogan-word--shirts">Shirts</h2>
    <div class="divider divider--second"></div>

    <div class="ring service-icon service-icon--swag">
      <div class="ring__inner">
        <div class="service-icon__art" role="img" aria-label="Line drawing of a cap, a mug and a tote bag"></div>
      </div>
    </div>
    <h2 class="slogan-word slogan-word--swag">Swag</h2>
  </section>
</main>
</body>
</html>
```